Business Cards for Valet Parking Company
Modern & Hospitality Oriented
Business Cards for Valet Parking Company - Automotive
Creative Brief
Simple
Colin Marsh
Owner & President
48270 E 9 Pine Avenue Suite 400 Farmington Hills, MI 48127
colin@orbitparkco.com
www.orbitparkco.com
On back of card: Anticipate, Invite & Engage

```html
<!DOCTYPE html>
<html lang="en">
<head>
<meta charset="utf-8">
<title>Orbit Park Co — Business Cards</title>
<link rel="stylesheet" href="https://fonts.googleapis.com/css2?family=Montserrat:wght@400;600;700&display=swap">
<style>
  :root {
    --backdrop: #d9dadc;
    --card: #ffffff;
    --ink: #1d1d1f;
    --muted: #4a4a4e;
    --accent-blue: #29a8e0;
    --band-dark: #2a2a2c;
    --rule: #9a9a9e;
  }
  * { box-sizing: border-box; margin: 0; padding: 0; }
  html, body {
    width: 1200px; height: 910px; overflow: hidden;
    background: var(--backdrop);
    font-family: "Montserrat", Arial, sans-serif;
    color: var(--ink);
  }
  .sheet { position: relative; width: 1200px; height: 910px; }
  .card {
    position: absolute; left: 300px; width: 600px; height: 343px;
    background: var(--card); border-radius: 22px; overflow: hidden;
    box-shadow: 0 6px 18px rgba(0,0,0,0.12);
  }
  .card--front { top: 70px; }
  .card--back { top: 497px; }

  .brand { display: flex; align-items: center; gap: 12px; }
  .brand__dot {
    width: 26px; height: 26px; border-radius: 50%;
    background: var(--accent-blue); flex: none;
  }
  .brand__name {
    font-weight: 700; letter-spacing: 3px; text-transform: uppercase;
    color: var(--ink);
  }
  .card--front .brand { position: absolute; left: 170px; top: 140px; }
  .card--front .brand__name { font-size: 34px; }
  .card--back .brand { position: absolute; left: 40px; top: 60px; }
  .card--back .brand__name { font-size: 28px; }

  .swoosh { position: absolute; left: 0; bottom: 0; width: 600px; height: 343px; }

  .divider {
    position: absolute; left: 392px; top: 46px; width: 1px; height: 200px;
    background: var(--rule);
  }
  .contact { position: absolute; left: 408px; top: 52px; width: 180px; }
  .contact__name {
    font-size: 12px; font-weight: 600; letter-spacing: 1px; text-transform: uppercase;
  }
  .contact__title { font-size: 9px; color: var(--muted); font-style: normal; margin-top: 2px; }
  .contact__address { font-size: 8.5px; color: var(--muted); margin-top: 14px; line-height: 1.45; font-style: normal; }
  .contact__list { list-style: none; margin-top: 14px; }
  .contact__item {
    display: flex; align-items: center; gap: 7px;
    font-size: 8.5px; color: var(--muted); margin-bottom: 7px;
  }
  .contact__icon { width: 10px; height: 10px; flex: none; fill: var(--muted); }
</style>
</head>
<body>
<main class="sheet">

  <section class="card card--front" aria-label="Card front">
    <div class="brand">
      <span class="brand__dot"></span>
      <span class="brand__name">Orbit Park Co</span>
    </div>
  </section>

  <section class="card card--back" aria-label="Card back">
    <svg class="swoosh" viewBox="0 0 600 343" aria-hidden="true">
      <path d="M0 300 C 150 250, 380 250, 600 270 L600 343 L0 343 Z" fill="var(--band-dark)"/>
      <path d="M0 292 C 150 236, 380 238, 600 262 L600 270 C 380 250, 150 250, 0 300 Z" fill="var(--card)"/>
      <path d="M0 262 C 140 212, 360 218, 600 246" fill="none" stroke="var(--accent-blue)" stroke-width="5"/>
    </svg>

    <div class="brand">
      <span class="brand__dot"></span>
      <span class="brand__name">Orbit Park Co</span>
    </div>

    <div class="divider"></div>

    <div class="contact">
      <p class="contact__name">Colin Marsh</p>
      <p class="contact__title">Owner &amp; President</p>
      <address class="contact__address">48270 E 9 Pine Avenue Suite 400<br>Farmington Hills, MI 48127</address>
      <ul class="contact__list">
        <li class="contact__item">
          <svg class="contact__icon" viewBox="0 0 10 10"><path d="M2 0.5h2l0.8 2.3-1.2 0.9a6 6 0 0 0 2.7 2.7l0.9-1.2 2.3 0.8v2a1 1 0 0 1-1 1A8.5 8.5 0 0 1 1 1.5a1 1 0 0 1 1-1z"/></svg>
          (248) 555-0142
        </li>
        <li class="contact__item">
          <svg class="contact__icon" viewBox="0 0 10 10"><path d="M2 0.5h2l0.8 2.3-1.2 0.9a6 6 0 0 0 2.7 2.7l0.9-1.2 2.3 0.8v2a1 1 0 0 1-1 1A8.5 8.5 0 0 1 1 1.5a1 1 0 0 1 1-1z"/></svg>
          (248) 555-0143
        </li>
        <li class="contact__item">
          <svg class="contact__icon" viewBox="0 0 10 10"><path d="M0.5 2h9v6h-9z M0.5 2l4.5 3.5 4.5-3.5" fill="none" stroke="var(--muted)" stroke-width="1"/></svg>
          colin@orbitparkco.com
        </li>
        <li class="contact__item">
          <svg class="contact__icon" viewBox="0 0 10 10"><circle cx="5" cy="5" r="4.3" fill="none" stroke="var(--muted)" stroke-width="1"/><path d="M0.7 5h8.6M5 0.7c-2.2 2.6-2.2 6 0 8.6M5 0.7c2.2 2.6 2.2 6 0 8.6" fill="none" stroke="var(--muted)" stroke-width="0.8"/></svg>
          www.orbitparkco.com
        </li>
      </ul>
    </div>
  </section>

</main>
</body>
</html>
```